Letterhead for New Orthopaedic Surgery Practice

My husband and I are starting our own practice named RB Spine & Vitality Center. We would like to create a nice simple but high class letterhead that doesn't use too much solid color ink when printing. I like the colors dark blue, gold, yellow. Open to other suggestions. We will need to list him and I both on the top of the letterhead. Here is the important information:
Lucinda Perrow, M.D. - Hand and Upper Extremity Surgery
Abena Quist, M.D. - Hip & Knee Replacement/General Orthopaedic Surgery
Location: 18735 North Harlow Pkwy
Coral Springs, FL 33071
Phone: 954-218-4650
Fax: 954-582-1346
Email: info@myrbspine.com

The only thing is that the phone and fax numbers will change once we get into our space. I just want to get the design started. I am including several documents which are my previous practice letterhead, my current procedure room letterhead, and our new Logo. The other letterheads are just for examples but please think outside of the box! We would love to see some great designs.

Colors
0054AA
0677BA
7BADD7
CADEEF
E8F1F8
0094D4
00A9DD
6FCCEA
C7EBF8
E9F6FB

Requirements
Must have
• class, elegance, luxury

```html
<!DOCTYPE html>
<html lang="en">
<head>
<meta charset="utf-8">
<title>RB Spine &amp; Vitality Center — Stationery</title>
<link rel="stylesheet" href="https://fonts.googleapis.com/css2?family=Marcellus&family=Arimo:wght@400;700&display=swap">
<style>
  :root {
    --backdrop: #d3dbde;
    --paper: #ffffff;
    --ink: #1a1a1a;
    --gold: #c29a4e;
    --brand-blue: #2a4899;
    --brand-blue-dark-bg: #3f63bf;
    --accent-cyan: #19b5e3;
    --navy-top: #241f63;
    --navy-bottom: #0e0e30;
    --card-text: #e6e8f2;
  }
  * { box-sizing: border-box; margin: 0; padding: 0; }
  html, body { width: 1200px; height: 1200px; overflow: hidden; }
  body { background: var(--backdrop); font-family: "Arimo", Arial, sans-serif; position: relative; }

  .sheet { position: absolute; overflow: hidden; }
  .wordmark { font-family: "Marcellus", Georgia, serif; font-weight: 400; color: var(--brand-blue); line-height: 1.1; }
  .wordmark-dot { display: inline-block; width: 6px; height: 6px; border-radius: 50%; background: currentColor; margin-left: 6px; vertical-align: middle; }
  .icon { width: 9px; height: 9px; fill: var(--gold); flex: none; }

  /* Letterhead */
  .letterhead { left: 111px; top: 34px; width: 479px; height: 678px; background: var(--paper); }
  .letterhead .head-mark { position: absolute; left: 31px; top: 24px; font-size: 15px; width: 150px; }
  .letterhead .contact { position: absolute; left: 348px; top: 40px; font-size: 8.6px; color: var(--ink); display: grid; gap: 3px; }
  .contact-row { display: flex; align-items: center; gap: 6px; }
  .letterhead .rule { position: absolute; left: 35px; right: 35px; top: 89px; height: 1px; background: var(--gold); }
  .signatory-name { font-family: "Marcellus", Georgia, serif; color: var(--gold); }
  .specialty { font-size: 6px; font-weight: 700; color: var(--ink); white-space: nowrap; }
  .specialty span { font-weight: 400; }
  .letterhead .signatory-top { position: absolute; top: 118px; }
  .letterhead .signatory-top .signatory-name { font-size: 15px; }
  .letterhead .signatory-left { left: 40px; text-align: left; }
  .letterhead .signatory-right { right: 35px; text-align: right; }
  .letterhead .date { position: absolute; right: 35px; top: 152px; font-size: 6px; color: var(--ink); }
  .letterhead .date b { color: var(--gold); }
  .letterhead .body-copy { position: absolute; left: 163px; top: 170px; width: 281px; font-size: 8.6px; line-height: 12.1px; color: var(--ink); text-align: justify; }
  .letterhead .body-copy p + p { margin-top: 12px; }
  .letterhead .signature { position: absolute; left: 162px; top: 453px; width: 82px; height: 32px; background: linear-gradient(90deg, #f3ead8, #eadbbb); border-radius: 3px; }
  .letterhead .signatory-bottom { position: absolute; left: 162px; top: 488px; }
  .letterhead .signatory-bottom .signatory-name { font-size: 13px; }
  .letterhead .footer-mark { position: absolute; left: 0; top: 560px; width: 190px; font-size: 26px; }
  .letterhead .address { position: absolute; left: 192px; top: 633px; font-size: 11px; color: var(--ink); display: flex; align-items: center; gap: 5px; }
  .letterhead .address .icon { width: 10px; height: 10px; }

  /* Folder cover */
  .cover { left: 618px; top: 34px; width: 480px; height: 679px; background: linear-gradient(180deg, var(--navy-top), var(--navy-bottom)); }
  .cover .cover-mark { position: absolute; left: 0; right: 0; top: 315px; text-align: center; font-size: 34px; color: var(--brand-blue-dark-bg); }
  .cover .cover-name { position: absolute; left: 0; right: 0; top: 627px; text-align: center; font-size: 11px; font-weight: 700; letter-spacing: 1.6px; color: #fff; }
  .cover .cover-name span { color: var(--accent-cyan); }

  /* Business cards */
  .card { top: 754px; height: 275px; border-radius: 12px; background: linear-gradient(120deg, var(--navy-top) 0%, var(--navy-bottom) 60%); }
  .card-front { left: 111px; width: 480px; }
  .card-front .card-mark { position: absolute; left: 0; right: 0; top: 118px; text-align: center; font-size: 30px; color: var(--brand-blue-dark-bg); }
  .card-back { left: 618px; width: 481px; }
  .card-back .side-mark { position: absolute; left: 30px; top: 126px; width: 180px; text-align: center; font-size: 19px; color: var(--brand-blue-dark-bg); }
  .card-back .details { position: absolute; left: 251px; top: 32px; color: var(--card-text); }
  .card-back .signatory-name { font-size: 20px; }
  .card-back .title { font-size: 12.5px; line-height: 15px; margin-top: 9px; letter-spacing: 0.3px; }
  .card-back .contact { margin-top: 14px; display: grid; gap: 4px; font-size: 13px; }
  .card-back .contact .icon { width: 11px; height: 11px; }
  .card-back .contact-row { gap: 10px; align-items: flex-start; }
  .card-back .contact-row .icon { margin-top: 3px; }
  .card-back .base-mark { position: absolute; left: 0; right: 0; top: 228px; text-align: center; font-size: 19px; color: #ffffff; }
</style>
</head>
<body>
  <svg width="0" height="0" style="position:absolute">
    <defs>
      <symbol id="i-phone" viewBox="0 0 10 10"><path d="M2.5 0h5a1 1 0 0 1 1 1v8a1 1 0 0 1-1 1h-5a1 1 0 0 1-1-1V1a1 1 0 0 1 1-1zm.3 1.2v6.3h4.4V1.2z"/></symbol>
      <symbol id="i-fax" viewBox="0 0 10 10"><path d="M2.5 0h5v2.5h-5zM1 3h8a1 1 0 0 1 1 1v3.5H8V10H2V7.5H0V4a1 1 0 0 1 1-1zm2 3.5v2.5h4V6.5z"/></symbol>
      <symbol id="i-send" viewBox="0 0 10 10"><path d="M10 0 0 4.2l3.6 1.3L8 2 4.5 6.4 5.8 10z"/></symbol>
      <symbol id="i-pin" viewBox="0 0 10 10"><path d="M5 0a3.6 3.6 0 0 0-3.6 3.6C1.4 6.3 5 10 5 10s3.6-3.7 3.6-6.4A3.6 3.6 0 0 0 5 0zm0 2a1.6 1.6 0 1 1 0 3.2A1.6 1.6 0 0 1 5 2z"/></symbol>
    </defs>
  </svg>

  <section class="sheet letterhead" aria-label="Letterhead">
    <div class="wordmark head-mark">RB Spine &amp; Vitality Center</div>
    <div class="contact">
      <div class="contact-row"><svg class="icon"><use href="#i-phone"/></svg>954-218-4650</div>
      <div class="contact-row"><svg class="icon"><use href="#i-fax"/></svg>954-582-1346</div>
      <div class="contact-row"><svg class="icon"><use href="#i-send"/></svg>info@myrbspine.com</div>
    </div>
    <div class="rule"></div>

    <div class="signatory-top signatory-left">
      <div class="signatory-name">Lucinda Perrow, M.D.</div>
      <div class="specialty">Hand <span>and</span> Upper Extremity Surgery</div>
    </div>
    <div class="signatory-top signatory-right">
      <div class="signatory-name">Abena Quist, M.D.</div>
      <div class="specialty">Hip &amp; Knee Replacement <span>/</span> General Orthopaedic Surgery</div>
    </div>
    <div class="date"><b>DATE :</b> 26-Sep-2025</div>

    <div class="body-copy">
      <p>Lorem ipsum dolor sit amet, consectetur adipiscing elit, sed do eiusmod tempor incididunt ut labore et dolore magna aliqua. Quis ipsum suspendisse ultrices gravida. Risus commodo viverra maecenas accumsan lacus vel facilisis. Lorem ipsum dolor sit amet, consectetur adipiscing elit, sed do eiusmod tempor incididunt ut labore et dolore magna aliqua. Quis ipsum suspendisse ultrices gravida.</p>
      <p>Lorem ipsum dolor sit amet, consectetur adipiscing elit, sed do eiusmod tempor incididunt ut labore et dolore magna aliqua.Quis ipsum suspendisse ultrices gravida. Risus commodo viverra maecenas accumsan lacus vel facilisis. Lorem ipsum dolor sit amet, consectetur adipiscing elit, sed do eiusmod tempor incididunt ut labore et dolore magna aliqua. Quis ipsum suspendisse ultrices gravida. Risus commodo viverra maecenas accumsan lacus vel facilisis.</p>
      <p>Lorem ipsum dolor sit amet, consectetur adipiscing elit, sed do eiusmod tempor incididunt ut labore et dolore magna aliqua. Quis ipsum suspendisse ultrices gravida. Risus commodo viverra maecenas accumsan lacus vel facilisis. Lorem ipsum dolor sit amet, consectetur adipiscing elit, sed do eiusmod tempor incididunt ut labore et dolore magna aliqua. Quis ipsum suspendisse ultrices gravida. Risus commodo viverra maecenas accumsan lacus vel facilisis.</p>
    </div>

    <div class="signature" role="img" aria-label="Handwritten signature of Lucinda Perrow"></div>
    <div class="signatory-bottom">
      <div class="signatory-name">Lucinda Perrow, M.D.</div>
      <div class="specialty">Hand <span>and</span> Upper Extremity Surgery</div>
    </div>

    <div class="wordmark footer-mark">RB Spine &amp; Vitality Center</div>
    <div class="address"><svg class="icon"><use href="#i-pin"/></svg>18735 North Harlow Pkwy Coral Springs, FL 33071</div>
  </section>

  <section class="sheet cover" aria-label="Presentation folder cover">
    <div class="wordmark cover-mark">RB Spine &amp;<br>Vitality Center</div>
    <div class="cover-name">RB SPINE &amp; <span>VITALITY</span> CENTER</div>
  </section>

  <section class="sheet card card-front" aria-label="Business card front">
    <div class="wordmark card-mark">RB Spine &amp;<br>Vitality Center</div>
  </section>

  <section class="sheet card card-back" aria-label="Business card back">
    <div class="wordmark side-mark">RB Spine &amp;<br>Vitality Center</div>
    <div class="details">
      <div class="signatory-name">Lucinda Perrow, M.D.</div>
      <div class="title">Board Certified Hand and<br>Upper Extremity Surgeon</div>
      <div class="contact">
        <div class="contact-row"><svg class="icon"><use href="#i-phone"/></svg>954-218-4650</div>
        <div class="contact-row"><svg class="icon"><use href="#i-fax"/></svg>954-582-1346</div>
        <div class="contact-row"><svg class="icon"><use href="#i-send"/></svg>info@myrbspine.com</div>
        <div class="contact-row"><svg class="icon"><use href="#i-pin"/></svg>18735 North Harlow Pkwy<br>Coral Springs, FL 33071</div>
      </div>
    </div>
    <div class="wordmark base-mark">RB Spine &amp; Vitality Center<span class="wordmark-dot"></span></div>
  </section>
</body>
</html>
```